Wine Label named: Amber Ridge

We are a wine producer, who wishes to launch a new premium wine called: Amber Ridge
Our winery is situated in a rolling hill, with slopes, where Amber Ridge exists in the property. One dates to the 15th century and the other more recent to the 18th century. Its a unique feature of the winery and we wish to create a label that represents these, but is NOT religious! Difficult task I know. Think you can pull it off? Let us see it! We start with one label, but the winner will have 5 more labels to design.

Target Market(s)

30-50 year old men

Industry/Entity Type

Wine

Colors

Designer to choose colors to be used in the design.

Requirements
Must have
• serious look and premium feel. name of the wine: Amber Ridge
Nice to have
• 2019 14% ABV
Should not have
• a religious look and feel

```html
<!DOCTYPE html>
<html lang="en">
<head>
<meta charset="utf-8">
<title>Amber Ridge Merlot — Label Pair</title>
<link rel="stylesheet" href="https://fonts.googleapis.com/css2?family=Cormorant+Garamond:wght@500&family=Montserrat:wght@500&display=swap">
<style>
  :root {
    --bg: #dcdcdb;
    --navy-light: #46557a;
    --navy-dark: #1f2843;
    --silver-light: #e4e4e4;
    --silver-dark: #b9b9b9;
    --gold: #c9a24a;
    --ink-dark: #3a3a3a;
    --ink-blue: #2f4a86;
    --white-text: #e6e9ef;
    --navy-art: #3a4a6e;
    --silver-art: #cdcdcd;
  }
  * { margin: 0; padding: 0; box-sizing: border-box; }
  html, body { width: 1200px; height: 1200px; overflow: hidden; background: var(--bg); }
  .stage {
    width: 1200px; height: 1200px;
    display: flex; justify-content: center; align-items: center; gap: 80px;
  }
  .label { position: relative; width: 440px; height: 580px; }
  .label svg.label-shape { position: absolute; inset: 0; }
  .emblem-art {
    position: absolute; top: 150px; left: 50%; transform: translateX(-50%);
    width: 370px; height: 250px; border-radius: 4px;
  }
  .label--navy .emblem-art { background: var(--navy-art); }
  .label--silver .emblem-art { background: var(--silver-art); }
  .wine-name {
    position: absolute; top: 458px; left: 0; right: 0; text-align: center;
    font-family: "Cormorant Garamond", serif; font-weight: 500;
    font-size: 34px; line-height: 40px; letter-spacing: 0.5px; text-transform: uppercase;
  }
  .label--navy .wine-name { color: var(--gold); }
  .label--silver .wine-name { color: var(--ink-dark); }
  .varietal {
    position: absolute; top: 505px; left: 0; right: 0; text-align: center;
    font-family: "Montserrat", sans-serif; font-weight: 500;
    font-size: 16px; line-height: 20px; letter-spacing: 6px; text-transform: uppercase;
  }
  .label--navy .varietal { color: var(--white-text); }
  .label--silver .varietal { color: var(--ink-blue); }
</style>
</head>
<body>
<main class="stage">
  <section class="label label--navy">
    <svg class="label-shape" width="440" height="580" viewBox="0 0 440 580">
      <defs>
        <linearGradient id="navyFill" x1="0" y1="0" x2="1" y2="0">
          <stop offset="0" stop-color="var(--navy-light)"/>
          <stop offset="1" stop-color="var(--navy-dark)"/>
        </linearGradient>
      </defs>
      <path d="M0 580 L0 215 Q0 70 220 0 Q440 70 440 215 L440 580 Z" fill="url(#navyFill)"/>
      <path d="M16 562 L16 218 Q16 86 220 20 Q424 86 424 218 L424 562 Z" fill="none" stroke="#8e96a8" stroke-width="1.5"/>
    </svg>
    <div class="emblem-art" role="img" aria-label="Gold emblem of two arches with stars above brushed rolling hills"></div>
    <h2 class="wine-name">Amber Ridge</h2>
    <p class="varietal">Merlot</p>
  </section>

  <section class="label label--silver">
    <svg class="label-shape" width="440" height="580" viewBox="0 0 440 580">
      <defs>
        <linearGradient id="silverFill" x1="0" y1="0" x2="1" y2="1">
          <stop offset="0" stop-color="var(--silver-light)"/>
          <stop offset="1" stop-color="var(--silver-dark)"/>
        </linearGradient>
      </defs>
      <path d="M0 580 L0 215 Q0 70 220 0 Q440 70 440 215 L440 580 Z" fill="url(#silverFill)"/>
      <path d="M16 562 L16 218 Q16 86 220 20 Q424 86 424 218 L424 562 Z" fill="none" stroke="#f2f2f2" stroke-width="1.5"/>
    </svg>
    <div class="emblem-art" role="img" aria-label="Gold emblem of two arches with stars above embossed rolling hills"></div>
    <h2 class="wine-name">Amber Ridge</h2>
    <p class="varietal">Merlot</p>
  </section>
</main>
</body>
</html>
```